Modular Cat Home Business Card

We need a business card for a modular and configurable cat playhouse, known as NookBox. NookBoxes can be integrated with human furniture. They come in cubes that are stackable, customizable and interchangeable.

Our name card should be in the shape of an isometric cube (not a normal business card size) with the NookBox logo inside the cube on one side of the namecard. If a home can be created inside the cube to show a homely environment, that could be an option. We are toying with the idea of having the cube side black and white and the flip side with our details, colorful. Our brand colours are pastel. They include pastel yellow, pink, purple, blue and orange. On the flip side, should be details including our name, position, email address, website, contact number.

The overall design should be clean, minimalistic, yet portray fun, happiness and quirky style. The product is design oriented so the name card should reflect likewise.

Target Market(s)

Cat Owners, Home owners, Mid 20s

Industry/Entity Type

Business

Contact Information for Business Card

Name, position, company name, phone number, email address, website. Name font should be bigger.

Colors
f8ba93
f9d9e8
ecdaeb
cee9f5
cfeae6
eaf2ce
fcf9cd
fce8d3
fbd4d5

Requirements
Must have
• The logo
• A variety of pastel colors
• A die cut in the form of a cube
Nice to have
• A home in the cube, to show furniture integration

```html
<!DOCTYPE html>
<html lang="en">
<head>
<meta charset="utf-8">
<title>NookBox Business Card</title>
<link rel="stylesheet" href="https://fonts.googleapis.com/css2?family=Arvo:wght@400;700&display=swap">
<style>
  :root {
    --paper: #ffffff;
    --cube-top: #faf7cc;
    --cube-left-a: #cadcbf;
    --cube-left-b: #d6e5bf;
    --cube-right-a: #faf7cb;
    --cube-right-b: #f8dc8c;
    --cutout-left: #c6dcbc;
    --cutout-right: #faf7cf;
    --brand-rose: #9a6460;
    --card-back: #59595b;
    --card-ink: #f2f2f2;
    --faint-mark: #e6e6e6;
    --print-peach: #fcd1a6;
    --print-cream: #fdf8dc;
    --print-sage: #bcd4aa;
    --print-grey: #929294;
  }
  html, body {
    margin: 0;
    padding: 0;
    width: 1200px;
    height: 1200px;
    overflow: hidden;
    background: var(--paper);
  }
  .sheet { display: block; width: 1200px; height: 1200px; }
  .brand-type { font-family: "Arvo", serif; }
  .contact-name { font-weight: 700; font-size: 12px; fill: var(--card-ink); letter-spacing: 0.4px; }
  .contact-line { font-weight: 400; font-size: 12px; fill: var(--card-ink); letter-spacing: 0.4px; }
  .contact-web { font-weight: 700; font-size: 12px; fill: var(--card-ink); letter-spacing: 0.4px; }
  .wordmark-back { font-size: 13px; fill: var(--card-ink); letter-spacing: 5px; }
  .wordmark-top { font-size: 20px; fill: var(--brand-rose); }
  .wordmark-faint { font-size: 20px; fill: var(--faint-mark); letter-spacing: 8px; }
</style>
</head>
<body>
<svg class="sheet" viewBox="0 0 1200 1200" xmlns="http://www.w3.org/2000/svg">
  <defs>
    <linearGradient id="leftFace" x1="0" y1="0" x2="1" y2="0">
      <stop offset="0" stop-color="var(--cube-left-a)"/>
      <stop offset="1" stop-color="var(--cube-left-b)"/>
    </linearGradient>
    <linearGradient id="rightFace" x1="0" y1="0" x2="1" y2="0">
      <stop offset="0" stop-color="var(--cube-right-a)"/>
      <stop offset="0.55" stop-color="var(--cube-right-a)"/>
      <stop offset="1" stop-color="var(--cube-right-b)"/>
    </linearGradient>
    <clipPath id="hexClip">
      <polygon points="819,505 1092,662 1092,976 819,1134 546,976 546,662"/>
    </clipPath>
  </defs>

  <!-- Cube front of the card -->
  <g class="cube-card">
    <polygon class="cube-face-top" points="365,102 636,258 366,414 95,258" fill="var(--cube-top)"/>
    <polygon class="cube-face-left" points="95,258 366,414 366,726 95,570" fill="url(#leftFace)"/>
    <polygon class="cube-face-right" points="366,414 636,258 636,570 366,726" fill="url(#rightFace)"/>
    <ellipse class="cube-opening-left" cx="232" cy="488" rx="78" ry="126" transform="rotate(-22 232 488)" fill="var(--cutout-left)" opacity="0.75"/>
    <ellipse class="cube-opening-right" cx="503" cy="492" rx="78" ry="126" transform="rotate(22 503 492)" fill="var(--cutout-right)" opacity="0.9"/>

    <g class="cube-prints">
      <ellipse role="img" aria-label="Paw print pattern" cx="358" cy="150" rx="22" ry="11" fill="var(--print-peach)"/>
      <ellipse role="img" aria-label="Paw print pattern" cx="194" cy="270" rx="22" ry="11" fill="var(--print-peach)"/>
      <ellipse role="img" aria-label="Paw print pattern" cx="398" cy="352" rx="22" ry="11" fill="var(--print-peach)"/>
      <ellipse role="img" aria-label="Paw print pattern" cx="582" cy="334" rx="13" ry="19" transform="rotate(30 582 334)" fill="var(--print-cream)"/>
      <ellipse role="img" aria-label="Paw print pattern" cx="136" cy="542" rx="13" ry="19" transform="rotate(-30 136 542)" fill="var(--print-sage)"/>
    </g>

    <g class="top-face-brand" transform="matrix(0.866,0.5,-0.866,0.5,372,250)">
      <rect x="-70" y="-30" width="22" height="22" fill="none" stroke="var(--brand-rose)" stroke-width="3"/>
      <text class="brand-type wordmark-top" x="-38" y="-11">NookBox</text>
    </g>
  </g>

  <!-- Faint brand mark -->
  <g class="faint-brand">
    <rect x="933" y="90" width="158" height="158" fill="none" stroke="var(--faint-mark)" stroke-width="4"/>
    <text class="brand-type wordmark-faint" x="1016" y="282" text-anchor="middle">NookBox</text>
  </g>

  <!-- Hexagon back of the card -->
  <g class="hex-card">
    <polygon points="819,505 1092,662 1092,976 819,1134 546,976 546,662" fill="var(--card-back)"/>
    <g class="hex-prints" clip-path="url(#hexClip)">
      <ellipse role="img" aria-label="Paw print pattern" cx="926" cy="580" rx="28" ry="30" fill="var(--print-grey)"/>
      <ellipse role="img" aria-label="Paw print pattern" cx="1008" cy="692" rx="28" ry="30" fill="var(--print-grey)"/>
      <ellipse role="img" aria-label="Paw print pattern" cx="912" cy="898" rx="28" ry="30" fill="var(--print-grey)"/>
      <ellipse role="img" aria-label="Paw print pattern" cx="984" cy="1028" rx="28" ry="30" fill="var(--print-grey)"/>
    </g>
    <g class="back-brand">
      <rect x="589" y="687" width="102" height="102" fill="none" stroke="var(--card-ink)" stroke-width="3"/>
      <text class="brand-type wordmark-back" x="589" y="810">NookBox</text>
    </g>
    <g class="contact-block brand-type">
      <text class="contact-name" x="587" y="840">Firstname Lastname</text>
      <text class="contact-line" x="587" y="854">Marketing Manager</text>
      <text class="contact-line" x="587" y="876">firstname@domain.com</text>
      <text class="contact-line" x="587" y="897">555 555 5555</text>
      <text class="contact-web" x="586" y="958">domain.com</text>
    </g>
  </g>
</svg>
</body>
</html>
```